Brunomalt1984 hat uns im Prinzip von der ersten Minute an begleitet, mitgedacht, Fragen gestellt, beraten und Vorschläge unterbreitet. Mehr Einsatzbereitsschaft, Interesse und Flexibilität kann man sich nicht wünschen. Außerdem hat hat er gleich drei verschiedene Designs in völlig unterschiedlichen Richtungen abgegeben. Und damit wir (als Laien) und besser vorstellen können was möglich ist, hat auch auch noch innerhalb jeden Designs etliche Variationen mit kleinen Unterschieden erstellt. Von ca. 100 Vorschlägen die wir insgesamt hatten, kamen alleine ca 40 nur von ihm. Nachdem sein Design gekürt war, ging es an den Feinschliff. Obwohl brunomalt schon gewonnen hatte, hat er sich nochmal viel Zeit genommen letzte Änderungen telefonisch zu besprechen. Am nächsten Tag war dann schon alles umgesetzt und das Design war perfekt. Besser geht einfach nicht!! Beim nächsten Mal: Direktauftrag ;) Oska

```html
<!DOCTYPE html>
<html lang="de">
<head>
<meta charset="utf-8">
<title>Edelstahl Draht – Etikett</title>
<link rel="stylesheet" href="https://fonts.googleapis.com/css2?family=Oswald:wght@400;500&display=swap">
<style>
  :root {
    --label-red: #e2001a;
    --label-red-dark: #b8001a;
    --label-type-red: #c5001c;
    --band-white: #f7f7f7;
    --band-shade: #dcdcdc;
    --ring-white: #ffffff;
    --page-bg: #ffffff;
  }
  html, body {
    margin: 0;
    padding: 0;
    width: 1200px;
    height: 1200px;
    overflow: hidden;
    background: var(--page-bg);
  }
  .label {
    display: block;
    width: 1200px;
    height: 1200px;
  }
  .label__caption {
    font-family: "Oswald", "Arial Narrow", sans-serif;
    font-weight: 400;
    font-size: 52px;
    fill: var(--ring-white);
  }
  .label__title,
  .label__subtitle,
  .label__spec {
    font-family: "Oswald", "Arial Narrow", sans-serif;
    font-weight: 500;
    fill: var(--label-type-red);
  }
  .label__title { font-size: 286px; }
  .label__subtitle { font-size: 204px; }
  .label__spec { font-size: 76px; }
  .label__icon {
    stroke: var(--label-type-red);
    fill: none;
    stroke-width: 6;
  }
</style>
</head>
<body>
<svg class="label" viewBox="0 0 1200 1200" xmlns="http://www.w3.org/2000/svg">
  <defs>
    <clipPath id="inner-disc">
      <circle cx="600" cy="600" r="568"/>
    </clipPath>
    <linearGradient id="band-sheen" x1="0" y1="0" x2="1" y2="1">
      <stop offset="0" stop-color="var(--band-white)"/>
      <stop offset="0.45" stop-color="var(--band-white)"/>
      <stop offset="0.62" stop-color="var(--band-shade)"/>
      <stop offset="0.8" stop-color="var(--band-white)"/>
      <stop offset="1" stop-color="var(--band-white)"/>
    </linearGradient>
    <marker id="arrow-head" viewBox="0 0 10 10" refX="8" refY="5" markerWidth="6" markerHeight="6" orient="auto-start-reverse">
      <path d="M0 0 L10 5 L0 10 z" fill="var(--label-type-red)"/>
    </marker>
  </defs>

  <!-- disc and ring -->
  <circle class="label__disc" cx="600" cy="600" r="596" fill="var(--label-red)" stroke="var(--label-red-dark)" stroke-width="4"/>
  <circle class="label__ring" cx="600" cy="600" r="574" fill="none" stroke="var(--ring-white)" stroke-width="4"/>

  <!-- white band -->
  <g clip-path="url(#inner-disc)">
    <rect class="label__band" x="0" y="336" width="1200" height="514" fill="url(#band-sheen)"/>
  </g>

  <!-- captions -->
  <text class="label__caption" x="600" y="270" text-anchor="middle" textLength="670" lengthAdjust="spacingAndGlyphs">xxxxx textfeld • xxxxx textfeld</text>
  <text class="label__caption" x="600" y="966" text-anchor="middle" textLength="670" lengthAdjust="spacingAndGlyphs">xxxxx textfeld • xxxxx textfeld</text>

  <!-- product name -->
  <text class="label__title" x="124" y="620" textLength="932" lengthAdjust="spacingAndGlyphs">EDELSTAHL</text>
  <text class="label__subtitle" x="136" y="826" textLength="400" lengthAdjust="spacingAndGlyphs">DRAHT</text>

  <!-- length spec -->
  <line class="label__icon" x1="676" y1="690" x2="858" y2="690" marker-start="url(#arrow-head)" marker-end="url(#arrow-head)"/>
  <text class="label__spec" x="1086" y="724" text-anchor="end">10 m</text>

  <!-- diameter spec -->
  <g class="label__icon">
    <circle cx="708" cy="782" r="22"/>
    <line x1="684" y1="808" x2="732" y2="756"/>
  </g>
  <text class="label__spec" x="1086" y="820" text-anchor="end" textLength="276" lengthAdjust="spacingAndGlyphs">0,03 mm</text>
</svg>
</body>
</html>
```